Business card design needed

I need a business card design for a dog walking, dog minding and dog training business. Please refer to my website for the basic company colours and fonts I'm after. Planning on a double sided card, so all information doesn't need to be on the 'front' side.
Cheers

Industry/Entity Type

Dog Training

Contact Information for Business Card

Meadow Paws - happy hounds
Rua 0498307164
meadowpawsdemo.com.au
-walking
-holiday stays
-onsite care
-training and behavioural consultations

```html
<!DOCTYPE html>
<html lang="en">
<head>
<meta charset="utf-8">
<title>Meadow Paws – business card options</title>
<link rel="stylesheet" href="https://fonts.googleapis.com/css2?family=Arimo:wght@400;700&display=swap">
<style>
  :root {
    --brand-orange: #d35322;
    --band-grey: #e9eaea;
    --text-grey: #555759;
    --text-dark: #2b2b2b;
    --card-white: #ffffff;
    --page: #ffffff;
    --photo-light: #f3efea;
    --photo-warm: #c98a55;
  }
  * { box-sizing: border-box; margin: 0; padding: 0; }
  html, body {
    width: 1143px; height: 1200px; overflow: hidden;
    background: var(--page);
    font-family: "Arimo", Arial, sans-serif;
  }
  .sheet { position: relative; width: 1143px; height: 1200px; }

  .option-number {
    position: absolute; font-size: 30px; color: var(--text-dark);
  }
  .option-number--one { left: 120px; top: 150px; }
  .option-number--two { left: 117px; top: 650px; }

  .card {
    position: absolute; width: 790px; height: 441px;
    border-radius: 38px; overflow: hidden;
    background: var(--card-white);
    box-shadow: 6px 8px 14px rgba(0,0,0,0.35), 0 0 3px rgba(0,0,0,0.2);
  }
  .card--one { left: 175px; top: 119px; }
  .card--two { left: 172px; top: 616px; }

  .card__top-band {
    position: absolute; left: 0; top: 0; width: 100%; height: 141px;
    background: var(--band-grey);
  }
  .card__photo {
    position: absolute; top: 0; right: 0; width: 233px; height: 156px;
    background: radial-gradient(ellipse at 50% 45%, var(--photo-warm) 0%, #e2c3a6 40%, var(--photo-light) 75%);
  }
  .card__wordmark {
    position: absolute; font-weight: 700; color: var(--brand-orange);
    text-transform: uppercase; letter-spacing: 1px; white-space: nowrap;
  }
  .card__tagline {
    position: absolute; left: 0; width: 790px; top: 150px; text-align: center;
    font-size: 20px; color: var(--text-grey);
  }
  .card__rule {
    position: absolute; left: 0; top: 182px; width: 100%; height: 5px;
    background: var(--brand-orange);
  }
  .contact-line {
    position: absolute; display: flex; align-items: center; gap: 10px;
    white-space: nowrap;
  }
  .contact-line svg { flex: none; }
  .card__services {
    position: absolute; left: 0; bottom: 0; width: 100%;
    background: var(--brand-orange); color: var(--card-white);
    text-align: center;
  }
  .card__services p { line-height: 1.25; }
  .dot { font-size: 0.6em; vertical-align: 0.2em; padding: 0 4px; }

  /* option one */
  .card--one .card__wordmark { left: 82px; top: 76px; font-size: 38px; }
  .card--one .contact-line { left: 0; width: 790px; justify-content: center; font-weight: 700; color: var(--text-grey); font-size: 26px; }
  .card--one .contact-line--phone { top: 230px; }
  .card--one .contact-line--web { top: 264px; }
  .card--one .card__services { height: 117px; padding-top: 22px; font-size: 25px; }

  /* option two */
  .card--two .card__wordmark {
    right: 246px; top: 64px; font-size: 37px; letter-spacing: 0.5px; text-align: right;
  }
  .card--two .card__web {
    position: absolute; right: 246px; top: 136px; font-size: 19px; font-weight: 700;
    color: var(--brand-orange); white-space: nowrap; text-align: right;
  }
  .card--two .contact-line { left: 245px; color: var(--text-dark); }
  .card--two .contact-line--phone { top: 203px; font-size: 27px; gap: 18px; }
  .card--two .contact-line--mail { top: 246px; font-size: 22px; gap: 12px; }
  .card--two .card__services { height: 134px; padding-top: 26px; font-size: 29px; }
</style>
</head>
<body>
<main class="sheet">
  <span class="option-number option-number--one">1</span>
  <section class="card card--one">
    <div class="card__top-band"></div>
    <div class="card__photo" role="img" aria-label="Photo of a puppy peeking over the card edge"></div>
    <div class="card__wordmark">Meadow Paws</div>
    <p class="card__tagline">happy hounds</p>
    <div class="card__rule"></div>
    <div class="contact-line contact-line--phone">
      <svg width="18" height="20" viewBox="0 0 18 20"><path d="M4 1 L7 5 L5 7 C6 10 8 13 11 15 L13 13 L17 16 L15 19 C8 18 2 11 1 4 Z" fill="var(--brand-orange)"/></svg>
      <span>Rua 0498307164</span>
    </div>
    <div class="contact-line contact-line--web">
      <svg width="18" height="18" viewBox="0 0 18 18"><g fill="none" stroke="var(--brand-orange)" stroke-width="1.5"><circle cx="9" cy="9" r="7.5"/><ellipse cx="9" cy="9" rx="3.5" ry="7.5"/><line x1="1.5" y1="9" x2="16.5" y2="9"/></g></svg>
      <span>meadowpawsdemo.com.au</span>
    </div>
    <div class="card__services">
      <p>walking <span class="dot">●</span> holiday stays <span class="dot">●</span> onsite care</p>
      <p>training and behavioural consultations</p>
    </div>
  </section>

  <span class="option-number option-number--two">2</span>
  <section class="card card--two">
    <div class="card__top-band"></div>
    <div class="card__photo" role="img" aria-label="Photo of a puppy peeking over the card edge"></div>
    <div class="card__wordmark">Meadow Paws</div>
    <div class="card__web">www.meadowpawsdemo.com.au</div>
    <div class="contact-line contact-line--phone">
      <svg width="18" height="20" viewBox="0 0 18 20"><path d="M4 1 L7 5 L5 7 C6 10 8 13 11 15 L13 13 L17 16 L15 19 C8 18 2 11 1 4 Z" fill="var(--brand-orange)"/></svg>
      <span>Rua 0498307164</span>
    </div>
    <div class="contact-line contact-line--mail">
      <svg width="24" height="16" viewBox="0 0 24 16"><g fill="none" stroke="var(--brand-orange)" stroke-width="1.5"><rect x="1" y="1" width="22" height="14"/><path d="M1 1 L12 9 L23 1"/></g></svg>
      <span>hello@meadowpawsdemo.com.au</span>
    </div>
    <div class="card__services">
      <p>walking <span class="dot">●</span> holiday stays <span class="dot">●</span> onsite care</p>
      <p>training and behavioural consultations</p>
    </div>
  </section>
</main>
</body>
</html>
```